Unique, market disruptive packaging design needed in Beverages Category

PELiqoMist - first to launch into African market!!
Need 3 design executions by tomorrow close of business 18th of December 2017

3 tiered branded strateg:
- 1 x High LSM, Niche brand
- 1 x Mid LSM Everyday brand
- 1 x Private label brand (very specific to my customer)

Have to be able to complete these 3 conceptual executions by tomorrow as i am seeing my customer with these concepts Tuesday morning at 10h00

FULL product brief to accompany

Thanks
Updates

I will take initial concept to Buyer, and will want to work with designer on the specific private label execution - give more information etc.

Target Market(s)

In the attached brief

Industry/Entity Type

Water Company

Other font styles liked:
• All info in the brief

Colors
0255a3
3176b5
85acd3
cedeed
cee9f5
85cae6
33a6d7
0692cd
ffffff

Requirements
Must have
• In the attached brief
Nice to have
• In the attached brief
Should not have
• In the attached brief

```html
<!DOCTYPE html>
<html lang="en">
<head>
<meta charset="utf-8">
<title>PELiqoMist – High LSM Carton</title>
<link href="https://fonts.googleapis.com/css2?family=Oswald:wght@700&family=Roboto:wght@400;700&family=Roboto+Condensed:wght@700&display=swap" rel="stylesheet">
<style>
  :root {
    --stage: #e4e4e4;
    --carton: #f4f6f8;
    --navy: #0f3a57;
    --teal: #12506a;
    --teal-light: #2f6f88;
    --ice: #cedeed;
    --mist: #cee9f5;
    --sky: #85cae6;
    --text: #3a4650;
    --ghost: #d6dbe0;
    --line: #a9c3d6;
    --white: #ffffff;
  }
  * { box-sizing: border-box; margin: 0; padding: 0; }
  html, body { width: 696px; height: 1200px; overflow: hidden; }
  body { background: var(--stage); position: relative; font-family: 'Roboto', sans-serif; color: var(--text); }

  .gable { position: absolute; left: 20px; top: 20px; width: 300px; height: 120px; background: var(--carton); border-bottom: 1px solid #d2d7dc; }
  .gable-band { position: absolute; left: 110px; top: 0; width: 80px; height: 120px; background: var(--teal); }
  .gable-band::after { content: ""; position: absolute; left: 8px; right: 8px; top: 0; bottom: 0; border-left: 2px solid var(--teal-light); border-right: 2px solid var(--teal-light); }

  .front-panel { position: absolute; left: 20px; top: 140px; width: 300px; height: 1040px; background: var(--carton); overflow: hidden; border-right: 1px solid #d2d7dc; }
  .droplet-texture { position: absolute; inset: 0; background: linear-gradient(180deg, #f7f9fb 0%, #e9eef2 55%, #dfe6ec 100%); }
  .water-drop-art { position: absolute; left: 0; top: 560px; width: 300px; height: 420px; background: radial-gradient(ellipse at 45% 60%, #6f95b3 0%, #a9c3d6 45%, #dbe6ee 75%, rgba(223,230,236,0) 100%); }
  .brand-name { position: absolute; left: -300px; top: 485px; width: 800px; height: 150px; transform: rotate(-90deg); font-family: 'Oswald', sans-serif; font-weight: 700; font-size: 140px; line-height: 150px; color: var(--navy); text-align: center; letter-spacing: -2px; white-space: nowrap; z-index: 1; }
  .tier-line { position: absolute; left: -110px; top: 400px; width: 700px; height: 40px; transform: rotate(-90deg); font-family: 'Roboto Condensed', sans-serif; font-weight: 700; font-size: 30px; line-height: 40px; color: var(--navy); text-align: center; white-space: nowrap; z-index: 2; }
  .net-label { position: absolute; left: 95px; top: 960px; width: 110px; height: 80px; background: var(--teal); color: var(--white); text-align: center; padding-top: 18px; font-size: 15px; line-height: 20px; }
  .net-label::before { content: ""; position: absolute; inset: 6px; border: 1px solid var(--teal-light); }

  .side-panel { position: absolute; left: 320px; top: 140px; width: 356px; height: 1040px; background: var(--carton); padding: 18px 14px; }
  .side-frame { border: 1px solid var(--line); height: 100%; padding: 14px 14px; font-size: 10.5px; line-height: 14px; }
  .ghost-name { font-family: 'Oswald', sans-serif; font-weight: 700; font-size: 40px; line-height: 46px; color: var(--ghost); text-align: center; margin-bottom: 14px; }
  .intro { text-align: center; margin-bottom: 12px; }
  .pill { display: block; width: 140px; margin: 6px auto 12px; background: var(--teal); color: var(--white); font-weight: 700; font-size: 11px; text-align: center; padding: 6px 0; border-radius: 3px; }
  .benefits { list-style: none; margin-bottom: 12px; }
  .benefits li { position: relative; padding-left: 12px; margin-bottom: 8px; }
  .benefits li::before { content: ""; position: absolute; left: 0; top: 5px; width: 4px; height: 4px; border-radius: 50%; background: var(--text); }
  .sizes-band { background: var(--teal); color: var(--white); text-align: center; padding: 8px 10px; border-radius: 4px; margin-bottom: 12px; }
  .section-title { font-weight: 700; font-size: 12px; text-align: center; color: var(--navy); margin-bottom: 8px; }
  .green-copy { text-align: center; margin-bottom: 12px; }
  .badges { display: flex; justify-content: center; gap: 14px; margin-bottom: 12px; }
  .badge { width: 34px; height: 34px; border-radius: 50%; border: 2px solid #3f9a4a; background: var(--white); }
  .certs { text-align: center; }
</style>
</head>
<body>
  <div class="gable"><div class="gable-band"></div></div>

  <section class="front-panel">
    <div class="droplet-texture" role="img" aria-label="Condensation droplets on a cool white surface"></div>
    <div class="water-drop-art" role="img" aria-label="Large water drop splash showing snowy mountains inside"></div>
    <div class="brand-name">PELiqoMist</div>
    <div class="tier-line">1 X HIGH LSM, NICHE BRAND</div>
    <div class="net-label">Net Wt.<br>200ml</div>
  </section>

  <section class="side-panel">
    <div class="side-frame">
      <div class="ghost-name">PELiqoMist</div>
      <p class="intro">Our Aseptic TerraFold cartons are made of renewable materials, recyclable paperboard and no refrigeration is needed when distributed and stored. Our Aseptic packages and ambient transportation allow our customers to capitalize on opportunities wherever they may arise around the globe.</p>
      <p class="intro">The Combination of the Aseptic process and packaging reduces waste, makes distribution extremely cost effective and convert our product into a consumer ready format as well as making it possible to reach consumers in remote locations.</p>
      <span class="pill">PRODUCT BENEFITS</span>
      <ul class="benefits">
        <li>Environmentally Friendly and bio-degradable</li>
        <li>Reduces the water footprint of any other water packaging by 500%</li>
        <li>Perfect for sports events, elderly, frail persons, kids, patients, toddlers and people on the go</li>
        <li>No contamination</li>
        <li>No preservatives</li>
        <li>Fits perfectly in your hand</li>
        <li>Controlled portion size</li>
        <li>Designed to fit perfectly in a lunch box or any other pre-set packaging</li>
        <li>Package designed for easy drink and squeeze</li>
        <li>Appeals to a wide range of the market</li>
        <li>Very cost effective</li>
        <li>Shelf life of 12 months</li>
      </ul>
      <p class="sizes-band">We are currently selling and distributing portion sizes in 100ml, 200ml and 1 Litre. We will produce to consumer needs if required.</p>
      <h2 class="section-title">ENVIRONMENT AND GOING GREEN</h2>
      <p class="green-copy">TerraFold packaging is made of 73% paperboard which is the main material used. It is a fully renewable resource that will bio-degrade into soil. Only 2.5% of water is fresh water and only 1% is accessible; the increase in population, social and economic activities in the world has affected the availability of fresh water resources. The water footprint ideology has increased due to scarcity of water and TerraFold water has assisted in reducing the water footprint of other packaged water by 500%.</p>
      <div class="badges"><span class="badge"></span><span class="badge"></span></div>
      <h2 class="section-title">PRODUCT AND SUPPLIER CERTIFICATION AND STANDARDS</h2>
      <p class="certs">Certimark certification conforming to the requirements of FSSC22000<br>The Vital Heart Trust<br>NHCB (National Halaal Certification Board)<br>Kashrut Certificate (Kosher status)</p>
    </div>
  </section>
</body>
</html>
```